I would like a stylish low key card that represents my Cedar Lodge. A boutique rental property . This property is of the highest standard and I wish the card to covey this without being old fashion

Industry/Entity Type

Boutique

Contact Information for Business Card

Tess Varlowe
0438207519
tess.varlowe@varlowe.com.au Cedar Lodge

```html
<!DOCTYPE html>
<html lang="en">
<head>
<meta charset="utf-8">
<title>Cedar Lodge — Business Card Concepts</title>
<link rel="stylesheet" href="https://fonts.googleapis.com/css2?family=Roboto:wght@300;400;500&display=swap">
<style>
  :root {
    --backdrop: #dededc;
    --card: #232323;
    --card-edge: #1b1b1b;
    --mark: #3b3e41;
    --icon: #4a4d50;
    --ink: #f2f2f2;
  }
  * { margin: 0; padding: 0; box-sizing: border-box; }
  html, body {
    width: 1200px; height: 900px; overflow: hidden;
    background: var(--backdrop);
    font-family: "Roboto", Arial, sans-serif;
  }
  .sheet { position: relative; width: 1200px; height: 900px; }
  .card {
    position: absolute; width: 413px; height: 234px;
    background: var(--card); border: 1px solid var(--card-edge);
  }
  .card--a { left: 166px; top: 195px; }
  .card--b { left: 622px; top: 195px; }
  .card--c { left: 166px; top: 470px; }
  .card--d { left: 622px; top: 470px; }

  .brand {
    position: absolute; color: var(--mark);
    font-weight: 500; letter-spacing: 1px; line-height: 1; white-space: nowrap;
  }
  .brand__line { display: block; font-size: 34px; }

  .card--a .brand { right: 58px; top: 30px; text-align: right; }
  .card--a .brand__line + .brand__line { margin-top: 2px; }
  .card--b .brand { left: 91px; top: 34px; }
  .card--b .brand__line + .brand__line { margin-left: 31px; margin-top: 2px; }
  .card--c .brand { left: 37px; top: 44px; font-size: 34px; }
  .card--d .brand {
    left: 45px; top: 38px; font-size: 37px; font-weight: 300;
    letter-spacing: 1.5px; text-transform: uppercase;
  }

  .contact { position: absolute; list-style: none; color: var(--ink); font-size: 14.5px; }
  .contact li { display: flex; align-items: center; height: 20px; }
  .contact svg { width: 14px; height: 12px; fill: var(--icon); flex: none; }

  .contact--right { right: 58px; top: 140px; text-align: right; }
  .contact--right li { justify-content: flex-end; }
  .contact--right svg { margin-left: 12px; }
  .contact--left li svg { margin-right: 8px; }

  .card--b .contact { left: 101px; top: 143px; }
  .card--b .contact svg { margin-right: 11px; }
  .card--c .contact { left: 31px; top: 131px; }
  .card--d .contact { left: 45px; top: 132px; }
</style>
</head>
<body>
<svg width="0" height="0" style="position:absolute">
  <defs>
    <symbol id="icon-person" viewBox="0 0 14 12"><circle cx="7" cy="3" r="3"/><path d="M1 12c0-3.5 2.5-5 6-5s6 1.5 6 5z"/></symbol>
    <symbol id="icon-phone" viewBox="0 0 14 12"><path d="M1 6.5C3 3.5 11 3.5 13 6.5l-1.8 1.6-1.8-1.2V5.6c-1.6-.5-3.2-.5-4.8 0v1.3L2.8 8.1z"/></symbol>
    <symbol id="icon-mail" viewBox="0 0 14 12"><path d="M0 2h14v1L7 7 0 3z"/><path d="M0 4.2l7 4 7-4V11H0z"/></symbol>
  </defs>
</svg>

<main class="sheet">
  <section class="card card--a">
    <p class="brand"><span class="brand__line">cedar</span><span class="brand__line">lodge</span></p>
    <ul class="contact contact--right">
      <li>Tess Varlowe<svg><use href="#icon-person"/></svg></li>
      <li>0438207519<svg><use href="#icon-phone"/></svg></li>
      <li>tess.varlowe@varlowe.com.au<svg><use href="#icon-mail"/></svg></li>
    </ul>
  </section>

  <section class="card card--b">
    <p class="brand"><span class="brand__line">cedar</span><span class="brand__line">lodge</span></p>
    <ul class="contact contact--left">
      <li><svg><use href="#icon-person"/></svg>Tess Varlowe</li>
      <li><svg><use href="#icon-phone"/></svg>0438207519</li>
      <li><svg><use href="#icon-mail"/></svg>tess.varlowe@varlowe.com.au</li>
    </ul>
  </section>

  <section class="card card--c">
    <p class="brand">cedar lodge</p>
    <ul class="contact contact--left">
      <li><svg><use href="#icon-person"/></svg>Tess Varlowe</li>
      <li><svg><use href="#icon-phone"/></svg>0438207519</li>
      <li><svg><use href="#icon-mail"/></svg>tess.varlowe@varlowe.com.au</li>
    </ul>
  </section>

  <section class="card card--d">
    <p class="brand">Cedar Lodge</p>
    <ul class="contact contact--left">
      <li><svg><use href="#icon-person"/></svg>Tess Varlowe</li>
      <li><svg><use href="#icon-phone"/></svg>0438207519</li>
      <li><svg><use href="#icon-mail"/></svg>tess.varlowe@varlowe.com.au</li>
    </ul>
  </section>
</main>
</body>
</html>
```